Ground-breaking AR Cyber Security Presentation

Clovendra LLC is a senior cadre of global business and technology advisors to enterprise clients on emerging technology, AR/VR solutions, and cyber security.

The desired PowerPoint (or Google Slides) presentation summarizes key points of a recently-completed, first-ever, comprehensive analysis of cyber security threats surrounding implementation of wearable Augmented Reality solutions (headsets/smart-glasses and software) in enterprise/industrial environments.

To be clear, we’re looking for both assistance with graphic design to illustrate key concepts, AND we’re looking for assistance with presentation format/style (color, layouts, consistent design elements, etc. so pitch looks pretty). We hope we can get that from one designer.

The target audience includes high-level business managers and executives of Fortune 500 companies concerned about unleashing a menagerie of unknown, untested wireless devices around their most-sensitive corporate assets and facilities.

The short message and theme: these unconventional connected devices (AR headsets and smart glasses) have opened up new and dangerous threat vectors into business data and operational assets, which must be understood and addressed by all key stakeholders and with the assistance of senior cyber security specialists (... like the Clovendra consulting team, for example)! Think: foreign hacktivists have been able to infiltrate and disrupt maintenance activities on a nuclear reactor. Or, nefarious actors have installed ransomware on the operational control system of a deep-water oil rig and are threatening to irreversibly damage the drill string causing a massive oil spill unless they're paid in 24 hours.

The presentation must be professional, but we highly welcome your interesting style twists. We prefer a mostly graphical presentation with text only where necessary - i.e. we're not going to be reading the slides; we're going to be telling a story punctuated with your high-quality graphics. The style should instill a bit of fear without being cartoony - REALLY tough for me to imagine since we're having to match our client's soothing Aqua color scheme. How do you make that scary? :) It should also, through polish of the presentation, convey a sense of confidence that our Clovendra team understands this unique topic better than anyone and is ready to help. Use your own created graphical illustrations or pics/images of the real-world.

We've provided our thoughts on design elements on each slide (colored BLUE; to be replaced with your designs). We've also provided talking points on the “Notes" pages of each slide (below) that we intend to personally refer to as we move through the presentation. That should help you understand the purpose of each slide.

Titles of slides can stay or be deleted, as necessary to convey the message on that page and we’re open to different verbiage if you think it will hit the points more effectively.

I can’t figure out how to get rid of the red border around each slide - please delete it.

From a color perspective, we want to be consistent with colors in the OTUM logo (lower right; our client). I did not select the correct colors for the text in this pitch - they are approximate & need to be corrected to be like the OTUM logo.

The background should stay as it is. I don’t like it, but it’s the client’s preference.

NOTE: The "OTUM" logo in the bottom right-hand corner needs to stay the same color and design as it is now. Move logos around, if desired.

ALL GRAPHICS PROVIDED MUST BE PUBLIC-DOMAIN OR HAVE USE RIGHTS THAT OTHERWISE CONVEY TO CLOVENDRA LLC

As a note, this project is going to be immediately followed with a separate flier project, then a full website refresh. Our logo needs help, also. Those are not part of this project but if we like your work, it would put you in position to possibly help with those if you're interested.

Target Market(s)

Industry/Entity Type

Business Software

Font styles to use
Sans Serif

Colors
3176b5
86cfc6
00a990
33b8a4
cfeae6
0255a3
85abd2
333333
5c5c5c

Requirements
Must have
• Professional feel. Somewhat constrained by colors in order to match client's logo. Client provided slide background, so we probably need to use it - this one could be optional. Really hoping the designer can provide some style so this doesn't end up being yet another boring business powerpoint.
Nice to have
• Need the most help with design of the graphics to help convey ideas on each slide. I took at stab at some examples just to give you an idea of what i was thinking.
Should not have
• Should not have any cartoon or unprofessional elements. No clutter or excess verbiage.

```html
<!DOCTYPE html>
<html lang="en">
<head>
<meta charset="utf-8">
<title>Cyber Security Essentials – Enterprise AR</title>
<link href="https://fonts.googleapis.com/css2?family=Roboto:wght@300;400;500;700&display=swap" rel="stylesheet">
<style>
:root{
  --ink:#1f3d47;
  --teal-dark:#1e4f5c;
  --teal:#3a6f78;
  --aqua:#33b8a4;
  --aqua-title:#2a9fb0;
  --text:#333333;
  --muted:#5c5c5c;
  --bg-a:#f7f8f8;
  --bg-b:#eceff0;
  --rule:#c9cfd1;
}
*{box-sizing:border-box;margin:0;padding:0}
html,body{width:1062px;height:1200px;overflow:hidden;background:#fff}
body{font-family:"Roboto",sans-serif;color:var(--text)}
.deck{display:grid;grid-template-columns:531px 531px;grid-template-rows:repeat(4,300px);width:1062px;height:1200px}
.slide{position:relative;overflow:hidden;background:linear-gradient(135deg,var(--bg-a),#ffffff 45%,var(--bg-b));border-right:1px solid var(--rule);border-bottom:1px solid var(--rule)}
.title{position:absolute;left:20px;top:24px;font-size:20px;font-weight:400;color:var(--ink);letter-spacing:.2px}
.title::before{content:"";position:absolute;left:-8px;top:3px;width:2px;height:20px;background:var(--ink)}
.page{position:absolute;left:480px;top:0;width:31px;height:26px;background:var(--teal-dark);color:#fff;font-size:9px;display:flex;align-items:center;justify-content:center;clip-path:polygon(0 0,100% 0,100% 100%,50% 82%,0 100%)}
.brand{position:absolute;left:14px;top:272px;display:flex;align-items:center;gap:4px;font-size:10px;font-weight:700;color:var(--teal-dark)}
.brand i{width:12px;height:12px;border-radius:50%;background:var(--teal-dark);display:block}
.client{position:absolute;left:436px;top:266px;font-size:26px;font-weight:700;color:var(--teal-dark);letter-spacing:1px}
.photo{position:absolute}

/* slide 1 */
.cover-band{position:absolute;left:0;top:46px;width:531px;height:200px;background:linear-gradient(90deg,#1d4d5c 0%,#2a5f70 50%,#4d7c8a 100%)}
.cover-title{position:absolute;left:30px;top:64px;color:#fff;font-size:21px;font-weight:400}
.cover-rule{position:absolute;left:30px;top:96px;width:236px;height:1px;background:#cfeae6}
.cover-sub{position:absolute;left:30px;top:105px;color:#86cfc6;font-size:17px;font-weight:700}
.cover-meta{position:absolute;left:36px;top:182px;color:#fff;font-size:13px;font-weight:700;line-height:16px}

/* slide 4 */
.danger-band{position:absolute;left:0;top:190px;width:531px;height:60px;background:var(--teal-dark)}
.danger-label{position:absolute;left:0;width:531px;top:8px;text-align:center;color:#fff;font-size:10px}
.danger-icon{position:absolute;top:28px;width:26px;height:26px}

/* slide 5 */
.subhead{position:absolute;left:0;width:531px;top:62px;text-align:center;color:var(--aqua-title);font-size:17px;font-weight:700}
.pillar{position:absolute;top:96px;width:128px;margin-left:-64px;text-align:center}
.pillar h3{font-size:11px;font-weight:700;color:var(--text);margin-bottom:6px}
.pillar .disc{width:84px;height:84px;border-radius:50%;background:var(--teal);margin:0 auto 10px;display:flex;align-items:center;justify-content:center}
.pillar p{font-size:9.6px;line-height:12px;color:var(--text)}

/* slide 6 */
.member{position:absolute;top:74px;width:126px;margin-left:-63px;text-align:center}
.member h3{font-size:11.5px;font-weight:700;color:var(--aqua-title);margin-bottom:6px}
.member .portrait{width:82px;height:82px;border-radius:50%;margin:0 auto 14px;background:radial-gradient(circle at 50% 40%,#8a8a8a,#2b2b2b);border:2px solid #333}
.member p{font-size:8.4px;line-height:10.6px;color:var(--text)}

/* slide 7 */
.orbit{position:absolute;width:74px;height:74px;margin:-37px 0 0 -37px;border-radius:50%;background:var(--teal);display:flex;align-items:center;justify-content:center}

/* slide 8 */
.framework{position:absolute;display:flex;align-items:center;justify-content:center;text-align:center}
.framework.top{left:107px;top:72px;width:335px;height:50px;background:var(--teal-dark);color:#fff;font-size:12.5px}
.framework.std{border:2px solid #1a2f4a;font-size:14px;font-weight:700;color:#1a2f4a;background:#fff}
</style>
</head>
<body>
<main class="deck">

<!-- 1 Cover -->
<section class="slide">
  <div class="cover-band" role="img" aria-label="Engineer wearing an augmented reality headset"></div>
  <h1 class="cover-title">Cyber Security Essentials</h1>
  <div class="cover-rule"></div>
  <h2 class="cover-sub">Enterprise Augmented Reality</h2>
  <p class="cover-meta">Tomas Halvorsen<br>CEO, Clovendra LLC<br>June 1, 2017</p>
  <div class="brand"><i></i>Clovendra</div>
  <div class="client">OTUM</div>
</section>

<!-- 2 Benefits -->
<section class="slide">
  <div class="page">2</div>
  <h2 class="title">Benefits of Enterprise AR</h2>
  <div class="photo" style="left:0;top:66px;width:295px;height:196px;background:linear-gradient(135deg,#6ea4d6,#2f6fae 60%,#9cc4e6)" role="img" aria-label="Worker using a VR headset with gesture controls"></div>
  <div class="photo" style="left:296px;top:66px;width:116px;height:98px;background:radial-gradient(circle,#d8dde0,#5c6870 70%)" role="img" aria-label="Jet engine turbine"></div>
  <div class="photo" style="left:413px;top:66px;width:118px;height:98px;background:linear-gradient(180deg,#0c2d5a,#1b4f8c)" role="img" aria-label="Offshore oil rig at night"></div>
  <div class="photo" style="left:296px;top:165px;width:235px;height:97px;background:linear-gradient(180deg,#2b3e6b,#b3783a 70%,#e7a64a)" role="img" aria-label="Power plant and transmission lines at dusk"></div>
  <div class="brand"><i></i>Clovendra</div>
  <div class="client">OTUM</div>
</section>

<!-- 3 Threats -->
<section class="slide">
  <div class="page">3</div>
  <h2 class="title">AR Is Also An Open Door To Threats!</h2>
  <div class="photo" style="left:132px;top:70px;width:248px;height:176px;border-radius:6px;background:#222;padding:10px">
    <div style="width:100%;height:100%;background:linear-gradient(180deg,#b32020,#8c1414)" role="img" aria-label="Ransomware warning screen demanding payment"></div>
  </div>
  <div class="photo" style="left:226px;top:246px;width:60px;height:30px;background:linear-gradient(180deg,#cfd3d5,#e9ecee);clip-path:polygon(25% 0,75% 0,100% 100%,0 100%)"></div>
  <div class="brand"><i></i>Clovendra</div>
  <div class="client">OTUM</div>
</section>

<!-- 4 Nightmare -->
<section class="slide">
  <div class="page">4</div>
  <h2 class="title">Nightmare Scenarios</h2>
  <div class="photo" style="left:0;top:58px;width:177px;height:132px;background:linear-gradient(135deg,#6b7a5a,#a8a9a0)" role="img" aria-label="Responders in protective suits spraying water"></div>
  <div class="photo" style="left:178px;top:58px;width:176px;height:132px;background:linear-gradient(135deg,#7b3a34,#5f6b4e)" role="img" aria-label="Rescue workers helping an injured person"></div>
  <div class="photo" style="left:355px;top:58px;width:176px;height:132px;background:linear-gradient(135deg,#6f7560,#c8b84a)" role="img" aria-label="Hazmat worker sampling near the shore"></div>
  <div class="danger-band">
    <div class="danger-label">Devastating Consequences</div>
    <svg class="danger-icon" style="left:71px" viewBox="0 0 26 26"><circle cx="13" cy="9" r="7" fill="#fff"/><rect x="8" y="15" width="10" height="9" fill="#fff"/><rect x="4" y="7" width="18" height="3" fill="#1e4f5c"/></svg>
    <svg class="danger-icon" style="left:162px" viewBox="0 0 26 26" fill="none" stroke="#fff" stroke-width="2"><circle cx="13" cy="8" r="5"/><circle cx="7" cy="17" r="5"/><circle cx="19" cy="17" r="5"/><circle cx="13" cy="14" r="2" fill="#fff"/></svg>
    <svg class="danger-icon" style="left:256px" viewBox="0 0 26 26" fill="none" stroke="#fff" stroke-width="2"><path d="M2 14 L13 5 L24 14"/><path d="M5 24 V14 M9 24 V16 M13 24 V12 M17 24 V17 M21 24 V20"/><path d="M4 8 L22 22"/></svg>
    <svg class="danger-icon" style="left:347px" viewBox="0 0 26 26" fill="#fff"><path d="M2 13 L13 3 L24 13 H21 V24 H5 V13 Z"/><rect x="11" y="16" width="4" height="8" fill="#1e4f5c"/></svg>
    <svg class="danger-icon" style="left:433px" viewBox="0 0 26 26" fill="none" stroke="#fff" stroke-width="2"><ellipse cx="11" cy="6" rx="8" ry="3"/><path d="M3 6 V18 Q11 22 19 18 V6 M3 12 Q11 16 19 12"/><path d="M17 18 L24 25 M24 18 L17 25"/></svg>
  </div>
  <div class="brand"><i></i>Clovendra</div>
  <div class="client">OTUM</div>
</section>

<!-- 5 Team needed -->
<section class="slide">
  <div class="page">5</div>
  <h2 class="title">You Need An Experienced Cyber Security Team</h2>
  <div class="subhead">The Clovendra Cyber Security Team Has</div>
  <div class="pillar" style="left:69px"><h3>Experience</h3>
    <div class="disc"><svg width="48" height="30" viewBox="0 0 48 30" fill="#fff"><circle cx="10" cy="9" r="5"/><circle cx="24" cy="7" r="6"/><circle cx="38" cy="9" r="5"/><path d="M2 28 Q10 14 18 28Z M14 28 Q24 10 34 28Z M30 28 Q38 14 46 28Z"/></svg></div>
    <p>100 years of leadership in emerging tech, data security, business innovation</p></div>
  <div class="pillar" style="left:198px"><h3>Knowledge</h3>
    <div class="disc"><svg width="40" height="44" viewBox="0 0 40 44" fill="#fff"><path d="M20 2 C32 2 38 10 36 20 L38 26 H34 V34 H24 V42 H10 V30 C4 26 2 18 6 10 C9 5 14 2 20 2Z"/></svg></div>
    <p>Hundreds of projects in mobility, connected devices, Industrial IoT, AR/VR/Wearables</p></div>
  <div class="pillar" style="left:329px"><h3>Leadership</h3>
    <div class="disc"><svg width="50" height="50" viewBox="0 0 50 50"><circle cx="25" cy="25" r="21" fill="none" stroke="#fff" stroke-width="3"/><path d="M25 9 L29 25 L25 41 L21 25Z M9 25 L25 21 L41 25 L25 29Z" fill="#fff"/></svg></div>
    <p>Leadership establishing global standards, best practices, frameworks &amp; testing protocols</p></div>
  <div class="pillar" style="left:460px"><h3>Connected</h3>
    <div class="disc"><svg width="44" height="44" viewBox="0 0 44 44" fill="#fff" stroke="#fff" stroke-width="3"><line x1="12" y1="22" x2="32" y2="10"/><line x1="12" y1="22" x2="32" y2="34"/><circle cx="12" cy="22" r="7"/><circle cx="32" cy="10" r="5"/><circle cx="32" cy="34" r="5"/></svg></div>
    <p>Wide professional network in global enterprise, industry organizations, &amp; government</p></div>
  <div class="brand"><i></i>Clovendra</div>
  <div class="client">OTUM</div>
</section>

<!-- 6 Meet the team -->
<section class="slide">
  <div class="page">6</div>
  <h2 class="title">Meet The Team</h2>
  <div class="member" style="left:69px"><h3>Tomas Halvorsen</h3><div class="portrait" role="img" aria-label="Portrait of Tomas Halvorsen"></div>
    <p>Project Management<br>Systems Engineering<br>AR / VR / Wearables<br>Mobility / Wireless<br>Enterprise IT Networks<br>Tech Commercialization</p></div>
  <div class="member" style="left:195px"><h3>Reid Lassiter</h3><div class="portrait" role="img" aria-label="Portrait of Reid Lassiter"></div>
    <p>Fmr Senior Director,<br>Strategic Innovation and<br>Standards for GTSB<br>Global Tech Standards<br>AR / VR / Wearables<br>Security &amp; Privacy Issues</p></div>
  <div class="member" style="left:327px"><h3>Dr. Julian Morrow</h3><div class="portrait" role="img" aria-label="Portrait of Dr. Julian Morrow"></div>
    <p>Ph.D Electrical Engr<br>Cyber Security Patents<br>Co-Author Industrial Connected<br>Security Framework (ICSF)<br>Co-Chair Industrial IoT<br>Security Standards WG</p></div>
  <div class="member" style="left:458px"><h3>Felix Corran</h3><div class="portrait" role="img" aria-label="Portrait of Felix Corran"></div>
    <p>Cyber-Warfare Ops, Navy<br>Army ARDX NIA NRB<br>AR / VR / Wearables<br>IIoT Cyber Security<br>Risk Frameworks<br>Threat Categorization</p></div>
  <div class="brand"><i></i>Clovendra</div>
  <div class="client">OTUM</div>
</section>

<!-- 7 AR vs Mobility -->
<section class="slide">
  <div class="page">7</div>
  <h2 class="title">AR Vs. Mobility</h2>
  <svg style="position:absolute;left:0;top:0" width="531" height="300"><circle cx="270" cy="175" r="122" fill="none" stroke="#1f3d47" stroke-width="1.2" stroke-dasharray="5 4"/></svg>
  <div class="photo" style="left:204px;top:32px;width:132px;height:268px;background:linear-gradient(180deg,#e6e8ea 0%,#2c3442 30%,#1f2630 100%);border-radius:50px 50px 0 0" role="img" aria-label="Businessman wearing a VR headset pointing forward"></div>
  <div class="orbit" style="left:170px;top:90px"><svg width="38" height="26" viewBox="0 0 38 26" fill="#fff"><rect x="2" y="4" width="8" height="20"/><rect x="11" y="2" width="8" height="22"/><rect x="20" y="2" width="8" height="22"/><rect x="29" y="4" width="7" height="20"/></svg></div>
  <div class="orbit" style="left:128px;top:162px"><svg width="40" height="32" viewBox="0 0 40 32" fill="#fff"><path d="M2 30 V14 L10 10 V16 L18 10 V16 L26 10 V2 H32 V30Z"/></svg></div>
  <div class="orbit" style="left:128px;top:250px"><svg width="36" height="36" viewBox="0 0 36 36" fill="none" stroke="#fff" stroke-width="3"><ellipse cx="18" cy="18" rx="15" ry="7"/><line x1="18" y1="3" x2="18" y2="33"/></svg></div>
  <div class="orbit" style="left:369px;top:90px"><svg width="40" height="34" viewBox="0 0 40 34" fill="#fff"><path d="M14 12 V8 a6 6 0 0 1 12 0 V12" fill="none" stroke="#fff" stroke-width="3"/><rect x="11" y="12" width="18" height="12" rx="2"/><text x="20" y="33" font-size="9" text-anchor="middle" font-family="Roboto,sans-serif">* * * *</text></svg></div>
  <div class="orbit" style="left:420px;top:162px"><svg width="40" height="32" viewBox="0 0 40 32" fill="none" stroke="#fff" stroke-width="3"><path d="M4 10 V4 H10 M30 4 H36 V10 M36 22 V28 H30 M10 28 H4 V22"/><path d="M8 16 Q20 6 32 16 Q20 26 8 16Z"/><circle cx="20" cy="16" r="4" fill="#fff"/></svg></div>
  <div class="orbit" style="left:406px;top:250px"><svg width="36" height="36" viewBox="0 0 36 36" fill="#fff"><rect x="6" y="28" width="16" height="5"/><rect x="12" y="16" width="4" height="12"/><circle cx="14" cy="14" r="4"/><rect x="14" y="8" width="14" height="4"/><path d="M28 4 L34 10 L28 14Z"/></svg></div>
  <div class="brand"><i></i>Clovendra</div>
  <div class="client">OTUM</div>
</section>

<!-- 8 Equivalence Pyramid -->
<section class="slide">
  <div class="page">8</div>
  <h2 class="title">Equivalence Pyramid</h2>
  <div class="framework top">OTUM Enterprise AR Cyber Security Framework</div>
  <div class="framework std" style="left:41px;top:132px;width:178px;height:52px">Stanorg</div>
  <div class="framework std" style="left:230px;top:132px;width:265px;height:52px">Corvane Security Framework</div>
  <div class="framework std" style="left:34px;top:194px;width:112px;height:52px">Veyra Cyber</div>
  <div class="framework std" style="left:154px;top:194px;width:143px;height:52px">Opsward</div>
  <div class="framework std" style="left:306px;top:194px;width:206px;height:52px;font-size:11px">Nordel Cyber Security Framework</div>
  <div class="brand"><i></i>Clovendra</div>
  <div class="client">OTUM</div>
</section>

</main>
</body>
</html>
```